New nutrition counseling business needs a flyer and logo design for marketing purposes

Need a new flyer for distribution to advertise and inform the public about new Dietetic Counseling service. The new business name is Harbor of Vigor with “Harbor” being the main name. It will provide nutrition consultation services to individuals who seek to change their dietary habits to achieve a variety of different health objectives. These objectives can include, but are not limited to weight management, enhanced athletic performance, improved health biomarkers, and reducing the risks or symptoms of chronic nutrition related diseases. The services provided include direct one on one counseling that entails health and nutrition assessments, evaluation of goals, and the determination of strategies to meet these goals. We would like to see designs that use an ocean color scheme with purple aspects as well. Color and logo ideas attached in uploads. Please include logo on the flyer as well.

Target Market(s)

General Population

Colors
0094D4
00A9DD
6FCCEA
C7EBF8
E9F6FB
00AB8E
00BBA5
67D7C9
C6EFE9
E9F9F6
6B429C
8869AF
B7A5CE
E3DAEB
F3F0F8

Requirements
Nice to have
• Pictures of nourishing foods, fruits, vegetables etc.
Should not have
• Do not include people in flyer or logo design

```html
<!DOCTYPE html>
<html lang="en">
<head>
<meta charset="utf-8">
<title>Harbor of Vigor – Nutrition Counseling Flyer</title>
<link href="https://fonts.googleapis.com/css2?family=Poppins:wght@400;500;600;700;800;900&display=swap" rel="stylesheet">
<style>
  :root{
    --blue:#2f86d3;
    --blue-deep:#2a7fcf;
    --sky:#6fbcf0;
    --green:#a2c96d;
    --purple:#6a3f9c;
    --ink:#151515;
    --white:#ffffff;
    --rule:#c9c9c9;
  }
  *{box-sizing:border-box;margin:0;padding:0}
  html,body{width:783px;height:1200px;overflow:hidden;background:#fff}
  body{font-family:'Poppins',sans-serif;color:var(--ink)}
  .flyer{position:relative;width:783px;height:1200px;overflow:hidden;background:var(--white)}
  .abs{position:absolute}
  .backdrop{left:0;top:0}

  .brand{left:52px;top:72px;display:flex;align-items:center;gap:12px}
  .brand-dot{width:46px;height:46px;border-radius:50%;background:var(--blue)}
  .brand-name{font-size:27px;font-weight:600;color:var(--blue);line-height:1}

  .title{left:52px;top:188px;line-height:1}
  .title-main{display:block;font-size:76px;font-weight:800;color:var(--blue);letter-spacing:1px}
  .title-sub{display:block;font-size:50px;font-weight:800;color:var(--ink);margin-top:2px}
  .title-sub .light{font-weight:400}

  .goal-band{left:0;top:347px;width:470px;height:130px;background:var(--purple)}
  .goal-head{left:57px;top:360px;display:flex;align-items:center;gap:12px}
  .goal-icon{width:28px;height:28px}
  .goal-label{font-size:27px;font-weight:700;color:var(--green)}
  .goal-text{left:57px;top:401px;font-size:16.5px;font-weight:700;color:var(--white);line-height:20px;width:300px}

  .owner{left:60px;top:490px}
  .owner-name{font-size:30px;font-weight:800;line-height:1.1}
  .owner-name .first{color:var(--blue)}
  .owner-role{font-size:20px;font-weight:500;line-height:1.2}
  .divider{left:60px;top:566px;width:652px;height:2px;background:var(--rule)}

  .credentials{left:60px;top:583px;width:370px;font-size:15px;line-height:19.5px}
  .credentials strong{color:var(--purple);font-weight:700}

  .license{left:446px;top:585px;width:266px;height:64px;border-radius:6px;overflow:hidden;background:var(--green)}
  .license-tag{position:absolute;left:0;top:0;width:150px;height:64px;background:var(--purple);clip-path:polygon(0 0,100% 0,72% 100%,0 100%)}
  .license-label{position:absolute;left:12px;top:11px;color:var(--white);font-size:19px;line-height:20px;font-weight:500}
  .license-label b{font-weight:700}
  .license-no{position:absolute;right:14px;top:13px;font-size:27px;font-weight:800;color:var(--ink)}

  .photo-card{left:62px;top:672px;width:264px;height:155px;border-radius:10px;background:linear-gradient(135deg,#f2f3f2,#e3e6e4 55%,#cfd6cd);box-shadow:0 3px 8px rgba(0,0,0,.25)}
  .photo-card::after{content:"";position:absolute;left:80px;top:25px;width:105px;height:105px;border-radius:50%;background:radial-gradient(circle,#e7a44a,#8fb54a 55%,#f7f7f7 62%)}

  .modes{left:62px;top:838px;font-size:19px;font-weight:700;line-height:23px}
  .modes .accent{color:var(--blue)}
  .dash{left:62px;top:900px;width:264px;border-top:1.5px dashed #777}

  .chat{left:64px;top:912px;font-size:20px;font-weight:700}
  .free{left:62px;top:934px;font-size:62px;font-weight:900;color:var(--purple);line-height:1}
  .free-note{left:212px;top:946px;font-size:13px;font-weight:700;line-height:16.5px}
  .details{left:62px;top:1004px;width:264px;height:58px;border:1.5px solid var(--ink);border-radius:12px;padding:8px 18px;font-size:16px;font-weight:700;line-height:19px}

  .services{left:359px;top:672px;width:354px;height:420px;border-radius:12px;overflow:hidden;background:var(--sky)}
  .services-head{position:absolute;left:0;top:0;width:100%;height:50px;background:var(--green);clip-path:polygon(0 0,100% 0,100% 100%,70% 100%,66% 86%,0 86%)}
  .services-title{position:absolute;left:26px;top:9px;font-size:22px;font-weight:500}
  .services-title b{font-weight:700}
  .service-list{position:absolute;left:26px;top:72px;list-style:none;width:310px}
  .service-list li{position:relative;padding-left:26px;font-size:14px;font-weight:500;line-height:17.5px;margin-bottom:14px}
  .service-list li::before{content:"";position:absolute;left:0;top:3px;width:12px;height:12px;border-radius:50%;background:var(--white)}
  .service-list li::after{content:"";position:absolute;left:3.5px;top:5.5px;width:3px;height:5px;border:solid var(--sky);border-width:0 2px 2px 0;transform:rotate(45deg)}

  .contact-label{left:62px;top:1104px;font-size:19px;font-weight:600;color:var(--white)}
  .phone{left:62px;top:1128px;display:flex;align-items:center;gap:6px;font-size:27px;font-weight:700;color:var(--white);letter-spacing:1px}
  .email{left:468px;top:1124px;display:flex;align-items:center;gap:10px;font-size:20px;font-weight:700;letter-spacing:1.2px}
</style>
</head>
<body>
<main class="flyer">

  <svg class="abs backdrop" width="783" height="1200" viewBox="0 0 783 1200" aria-hidden="true">
    <path d="M350 0H783V545C760 520 740 505 700 495L460 210C440 120 410 55 350 0Z" fill="var(--green)"/>
    <path d="M315 0C335 25 355 38 385 48C420 60 440 75 455 110" fill="none" stroke="var(--sky)" stroke-width="16"/>
    <path d="M710 470C745 490 770 510 783 540" fill="none" stroke="var(--sky)" stroke-width="14"/>
    <circle cx="581" cy="246" r="214" fill="none" stroke="#fff" stroke-width="2.5" stroke-dasharray="10 7"/>
    <path d="M0 1088H320C390 1088 410 1188 500 1192H783V1200H0Z" fill="var(--blue-deep)"/>
    <path d="M335 1086C395 1092 415 1186 520 1190" fill="none" stroke="var(--green)" stroke-width="6"/>
  </svg>

  <div class="abs goal-band"></div>

  <svg class="abs" style="left:380px;top:48px" width="400" height="600" viewBox="380 48 400 600" role="img" aria-label="Photo of a fresh salad plate with a bowl of greens, a green apple, pink hand weights and a tape measure">
    <circle cx="581" cy="246" r="196" fill="#fff"/>
    <circle cx="581" cy="246" r="180" fill="url(#salad)"/>
    <ellipse cx="600" cy="570" rx="180" ry="60" fill="url(#extras)"/>
    <defs>
      <radialGradient id="salad" cx="50%" cy="45%" r="55%">
        <stop offset="0" stop-color="#8cae4a"/>
        <stop offset=".55" stop-color="#5f8f36"/>
        <stop offset=".85" stop-color="#c9733b"/>
        <stop offset="1" stop-color="#eeeeee"/>
      </radialGradient>
      <linearGradient id="extras" x1="0" x2="1">
        <stop offset="0" stop-color="#dfe6d8"/>
        <stop offset=".35" stop-color="#8cc63f"/>
        <stop offset=".7" stop-color="#d1266f"/>
        <stop offset="1" stop-color="#6d9a3a"/>
      </linearGradient>
    </defs>
  </svg>

  <div class="abs brand">
    <span class="brand-dot"></span>
    <span class="brand-name">Harbor of Vigor</span>
  </div>

  <h1 class="abs title">
    <span class="title-main">HARBOR</span>
    <span class="title-sub"><span class="light">OF</span> VIGOR</span>
  </h1>

  <div class="abs goal-head">
    <svg class="goal-icon" viewBox="0 0 28 28" aria-hidden="true">
      <circle cx="14" cy="14" r="13" fill="#6fbcf0"/>
      <circle cx="14" cy="14" r="8.5" fill="none" stroke="#fff" stroke-width="1.6"/>
      <circle cx="14" cy="14" r="4.5" fill="none" stroke="#fff" stroke-width="1.6"/>
      <circle cx="14" cy="14" r="1.5" fill="#fff"/>
    </svg>
    <span class="goal-label">GOAL</span>
  </div>
  <p class="abs goal-text">HELPING CLIENTS FOSTER POSITIVE NUTRITION PRACTICES FOR A HEALTHIER LIFESTYLE</p>

  <div class="abs owner">
    <p class="owner-name"><span class="first">MAREN</span> SOLACE</p>
    <p class="owner-role">OWNER</p>
  </div>
  <div class="abs divider"></div>

  <p class="abs credentials"><strong>Credentials:</strong> Master of Science in Dietetics and Nutrition, Registered Dietitian (RD), Licensed Dietitian Nutritionist (LDN)</p>

  <div class="abs license">
    <div class="license-tag"></div>
    <p class="license-label"><b>LICENSE</b><br>NUMBER</p>
    <p class="license-no">ND 40218</p>
  </div>

  <div class="abs photo-card" role="img" aria-label="Photo of a bowl of salad on a light table with avocado and tomatoes"></div>
  <p class="abs modes">Both in person and virtual<br><span class="accent">consultations are offered</span></p>
  <div class="abs dash"></div>

  <p class="abs chat">Let’s Chat!</p>
  <p class="abs free">FREE</p>
  <p class="abs free-note">15-MINUTE<br>INTRODUCTORY<br>CONSULTATION</p>
  <p class="abs details">To discuss program details and rates</p>

  <section class="abs services">
    <div class="services-head"></div>
    <h2 class="services-title">OUR <b>SERVICES</b></h2>
    <ul class="service-list">
      <li>Medical Nutrition Therapy for chronic conditions such as diabetes, hypertension, high cholesterol, and more</li>
      <li>Weight Management</li>
      <li>Healthy Eating and Meal Planning</li>
      <li>Nutrition for Athletic Performance</li>
      <li>Pre and Post Natal Nutrition</li>
      <li>Personalized meal plans uniquely catered to each individual</li>
      <li>Highly collaborative approach to help you meet your goals</li>
    </ul>
  </section>

  <p class="abs contact-label">CONTACT INFORMATION</p>
  <p class="abs phone">
    <svg width="18" height="18" viewBox="0 0 24 24" aria-hidden="true"><path fill="#8a5cc2" d="M6.6 10.8a15.1 15.1 0 0 0 6.6 6.6l2.2-2.2a1 1 0 0 1 1-.25 11.4 11.4 0 0 0 3.6.57 1 1 0 0 1 1 1V20a1 1 0 0 1-1 1A17 17 0 0 1 3 4a1 1 0 0 1 1-1h3.5a1 1 0 0 1 1 1c0 1.25.2 2.45.57 3.57a1 1 0 0 1-.25 1z"/></svg>
    555-014-2287
  </p>
  <p class="abs email">
    <svg width="22" height="16" viewBox="0 0 22 16" aria-hidden="true"><rect width="22" height="16" rx="1.5" fill="#6a3f9c"/><path d="M1 1.5l10 7.5 10-7.5" fill="none" stroke="#fff" stroke-width="1.6"/></svg>
    maren@solacerd.net
  </p>

</main>
</body>
</html>
```